New Website for QWRB Holdings (Property Leasing Company in New Haven)

Design a fully functioning website for a real estate property leasing company. The company has a few properties in New Haven, CT and would like to provide an option for its tenants to pay their rent online. The company should have the ability to generate unique account log in username and password for its tenants so they can make online payments through ACH the website. (The ACH processing part will be coordinated with the bank).

Please take a look at all the pictures I uploaded of New Haven especially the area around Marlow College, you will find that the general style is Gothic and charming.

Also please make use of the pictures of the two properties I have attached to the description.

Please keep Holdings page, Contact Us Page , About Us Page, and please add a page entitled "Tenants".

On the Holdings page I would like to see on the left hand side an interactive map of new haven (Please see a map attached), split by New Haven's neighbourhoods, and showing my properties as pins of sort on the map (I can send you the addresses of the properties upon request). On the same page on the right side I want to see a drop down menu that includes list of New Haven Neighbourhoods. When a neighbourhood is selected you can see in the space underneath the drop-down menu the properties we have in that neighbourhood in large thumbnail format. Also on the map you can see the pins corresponding to those properties change colour. A user can either click on the pin or on the thumbnails to have view more pictures of the property and some details in text.

The tenants page should prompt a login to access- I like your idea of having the company name in two colours, one for QWRB and another for Holdings.Please let me know if you have any questions along the way

-------------------------------------------------------------------------------
Property Descriptions for Holdings Page
The Larch Lodge,

Neighbourhood: Westville
Name: Silas Brennaway House
Building Style: Queen Anne Style
Address: 418 Pellwin Road, New Haven, CT 06515
Number of Units: 3
Unit Names: Unit 1, Unit 2, Unit 3

Property Description

This Westiville home was built in 1897, historically known as The Silas Brennaway House, it is an example of the Queen Anne style. The large carriage house is still intact and sits in the lovely, expansive back garden! An outstanding architectural feature of the house is the turret, giving the home prominence on Pellwin Road. This well maintained home has renovated kitchens in all units, the first floor has granite and red oak cabinetry. New baths and central air in all apartments. All newer mechanicals for each unit, all natural gas. The entire house has replacement windows. The new back deck overlooks the back garden and carriage house. The front steps and porch have also been rebuilt. Roof has 30 year architectural singles and approximately 15 years old, the chimney has just been lined.

Unit 1 Description:

2 Bedrooms, 6 rooms in total.
Amenities: Dishwasher, Central Air, Gas Heating, Porch

Unit 2 Description:

2 Bedrooms, 5 rooms in total.
Amenities: Dishwasher, Central Air, Gas Heating, Balcony

Unit 3 Description:

2 Bedrooms, 4 rooms in total.
Amenities: Dishwasher, Central Air, Gas Heating

The Fern Lodge:

Neighbourhood: East Rock
Name: 64 Birchmere
Building Style: Victorian
Address: 64 Birchmere Lane, New Haven, CT 06511
Number of Units: 2
Unit Names: Unit 1, and Unit 2

Property Description

East Rock incredibly charming newly renovated 2 family on quiet tree-lined block. Tenants are responsible for all utilities (gas heat, electricity and cable). Small pets are possible with landlord approval. Tenants has use of shared yard, laundry in the basement and on street parking only. Located steps away from gourmet markets & minutes to Downtown New Haven, Marlow & local hospitals. Fascinating backyard. This is a feel good house!

Unit 1 Description:

Area:
1100 soft, 3 Bedrooms, 5 rooms in total.
Amenities: In unit Washer and Dryer, Central Air, Gas Heating, Porch, Backyard

Unit 2 Description:

Area: 2,820 sqft
5 Bedrooms, 8 rooms in total.
Amenities: In unit Washer and Dryer, Dishwasher, Central Air, and Gas Heating

Target Market(s)

1-3 bedroom Renting Market around Marlow College and New Haven Community

Industry/Entity Type

Real Estate

Coding

Coded - Design and coding required

Number of Pages Required

4 page

Font styles to use
Other font styles liked:
• Helvetica

Colors
85cae6
cee9f5
d9d9d9
9d9d9d

Requirements
Must have
• Payment page with login (accounts can only be created by administrator)
• A page showcasing the properties (Professional photos to be uploaded shortly)
• A page for technical support, contact information and so forth
• Home page
Nice to have
• A professional, but stylish design. Not too colourful, something with pastel colours
Should not have
• A lot of colours, any pop-ups,

```html
<!DOCTYPE html>
<html lang="en">
<head>
<meta charset="utf-8">
<title>QWRB Holdings</title>
<link rel="stylesheet" href="https://fonts.googleapis.com/css2?family=Questrial&family=Open+Sans:wght@400;600;700&display=swap">
<style>
:root{
  --blue:#3ea6dc;
  --blue-light:#85cae6;
  --blue-pale:#cee9f5;
  --grey:#d9d9d9;
  --grey-mid:#9d9d9d;
  --ink:#3a3f45;
  --text:#5b6066;
  --dark:#23282e;
  --white:#ffffff;
}
*{box-sizing:border-box;margin:0;padding:0}
html,body{width:711px;height:1200px;overflow:hidden}
body{position:relative;background:var(--white);font-family:"Open Sans",Arial,sans-serif;color:var(--text)}
.abs{position:absolute}
.heading{font-family:"Questrial",Arial,sans-serif}

/* hero */
.hero{left:0;top:0;width:711px;height:410px;overflow:hidden}
.hero-photo{position:absolute;inset:0;background:linear-gradient(180deg,#9eb3c2 0%,#b9c6cd 28%,#8f6d58 52%,#6b5447 70%,#4d5a44 100%)}
.hero-shade{position:absolute;inset:0;background:linear-gradient(180deg,rgba(20,30,40,.55) 0%,rgba(20,30,40,0) 22%,rgba(20,30,40,0) 70%,rgba(20,30,40,.45) 100%)}
.hero-cut{position:absolute;left:0;bottom:0}
.brand{left:38px;top:12px;display:flex;align-items:center;gap:8px;color:var(--white)}
.brand-mark{width:26px;height:26px;background:var(--white)}
.brand-name{font-family:"Questrial",Arial,sans-serif;font-size:19px;line-height:18px;color:var(--white);letter-spacing:.5px}
.social-top{left:474px;top:11px;display:flex;gap:8px}
.social-top span{width:16px;height:16px;background:var(--white);border-radius:2px}
.phone-top{left:552px;top:9px;display:flex;align-items:center;gap:6px;color:var(--white);font-size:12px;font-weight:600}
.phone-top svg{width:20px;height:20px}
.nav{left:398px;top:38px;display:flex;gap:20px}
.nav a{font-family:"Questrial",Arial,sans-serif;font-size:11px;color:var(--white);text-decoration:none;padding-bottom:4px;letter-spacing:.4px}
.nav a.active{border-bottom:2px solid var(--blue)}
.tagline{left:0;top:352px;width:711px;text-align:center;color:var(--white);font-weight:700;font-size:19px;text-shadow:0 1px 3px rgba(0,0,0,.5)}

/* about */
.about-title{left:0;top:424px;width:711px;text-align:center;font-size:21px;color:var(--ink);letter-spacing:.5px}
.about-title b{font-weight:400;color:var(--blue)}
.rule{left:78px;width:555px;height:1px;background:var(--grey)}
.about-copy{left:78px;top:468px;width:555px;font-size:8.4px;line-height:11.5px;text-align:center;color:var(--text)}
.read-more{left:0;top:536px;width:711px;text-align:center;font-size:10px;font-weight:700;color:var(--ink)}

/* featured */
.featured{left:0;top:562px;width:711px;height:320px;background:linear-gradient(180deg,#2b3036 0%,#3c3a36 40%,#5a4a3a 75%,#2a2f33 100%)}
.featured-title{left:0;top:596px;width:711px;text-align:center;font-size:21px;color:var(--white);letter-spacing:.5px}
.featured-title b{font-weight:400;color:var(--blue)}
.arrow{top:724px;width:18px;height:18px}
.card{top:656px;width:128px}
.card-photo{width:128px;height:114px;border:2px solid var(--white)}
.card-title{margin-top:8px;font-size:10px;font-weight:700;color:var(--white)}
.card-text{margin-top:3px;font-size:7px;line-height:9px;color:#d8dde2}
.pay-btn{display:inline-block;margin-top:6px;background:var(--white);color:var(--ink);font-size:8px;font-weight:600;padding:2px 6px;border-radius:2px}

/* lower */
.lower{left:0;top:882px;width:711px;height:258px;background:linear-gradient(160deg,#f1f3f3 0%,#e4e8e6 45%,#eef1ef 100%)}
.panel{top:912px;background:rgba(210,213,215,.9)}
.panel-head{font-family:"Questrial",Arial,sans-serif;font-size:14px;color:var(--ink);padding:8px 10px;letter-spacing:.6px;background:rgba(190,194,197,.9)}
.panel-sub{font-size:7px;color:var(--text);padding:6px 10px 2px}
.field{margin:5px 10px 0;width:180px;height:14px;background:var(--white);font-size:7px;color:var(--grey-mid);padding:2px 5px}
.field.tall{height:30px}
.submit{margin:8px 10px 10px 90px;display:inline-block;background:var(--dark);color:var(--white);font-size:8px;font-weight:700;padding:3px 10px;letter-spacing:.5px}
.contact-row{display:flex;align-items:center;gap:10px;padding:10px 12px 0}
.contact-row svg{width:24px;height:24px;flex:none}
.contact-row p{font-size:9px;font-weight:600;color:var(--ink);line-height:12px}

/* footer */
.footer{left:0;top:1128px;width:711px;height:72px;background:var(--blue-pale)}
.footer-links{left:78px;top:1146px;display:flex;gap:16px;font-size:8px;color:var(--ink)}
.copyright{left:78px;top:1178px;font-size:7.5px;color:var(--text)}
.footer-brand{left:440px;top:1138px;width:195px;text-align:right;font-family:"Questrial",Arial,sans-serif;font-size:22px;color:var(--blue);letter-spacing:.6px}
.social-foot{left:545px;top:1172px;display:flex;gap:10px}
.social-foot span{width:18px;height:18px;background:var(--grey-mid);border-radius:2px}
</style>
</head>
<body>

<header class="abs hero">
  <div class="hero-photo" role="img" aria-label="City skyline with brick towers and trees"></div>
  <div class="hero-shade"></div>
  <svg class="hero-cut" width="711" height="40" viewBox="0 0 711 40"><polygon points="0,12 711,40 711,40 0,40" fill="#ffffff"/></svg>
</header>

<div class="abs brand"><span class="brand-mark"></span><span class="brand-name">QWRB<br>HOLDINGS</span></div>
<div class="abs social-top"><span></span><span></span><span></span></div>
<div class="abs phone-top">
  <svg viewBox="0 0 20 20"><circle cx="10" cy="10" r="9" fill="none" stroke="#fff" stroke-width="1.5"/><path d="M7 5.5l1.6 2.2-1 1.2c.6 1.3 1.6 2.3 2.9 2.9l1.2-1 2.2 1.6-.8 1.8c-3.7-.2-6.8-3.3-7-7z" fill="#fff"/></svg>
  012-345-6789
</div>
<nav class="abs nav"><a class="active">HOME</a><a>ABOUT</a><a>HOLDINGS</a><a>CONTACT US</a></nav>
<p class="abs tagline">We Provide Real Estate Property Leasing Company</p>

<h2 class="abs heading about-title">ABOUT <b>QWRB HOLDINGS</b></h2>
<div class="abs rule" style="top:456px"></div>
<p class="abs about-copy">Lorem ipsum dolor sit amet, consectetuer adipiscing elit, sed diam nonummy nibh euismod tincidunt ut laoreet dolore magna aliquam erat volutpat. Ut wisi enim ad minim veniam, quis nostrud exerci tation ullamcorper suscipit lobortis nisl ut aliquip ex ea commodo consequat. Duis autem vel eum iriure dolor in hendrerit in vulputate velit esse molestie consequat, vel illum dolore eu feugiat nulla facilisis at vero eros et accumsan et iusto odio dignissim qui blandit praesent luptatum zzril delenit augue duis dolore te feugait nulla facilisi.</p>
<p class="abs read-more">Read More &#187;</p>

<section class="abs featured" role="img" aria-label="Evening view of town rooftops and autumn trees"></section>
<h2 class="abs heading featured-title">FEATURED <b>PROPERTY</b></h2>
<svg class="abs arrow" style="left:30px" viewBox="0 0 18 18"><path d="M12 3L6 9l6 6" fill="none" stroke="#fff" stroke-width="2"/></svg>
<svg class="abs arrow" style="left:663px" viewBox="0 0 18 18"><path d="M6 3l6 6-6 6" fill="none" stroke="#fff" stroke-width="2"/></svg>

<article class="abs card" style="left:78px">
  <div class="card-photo" role="img" aria-label="Victorian house facade" style="background:linear-gradient(160deg,#8a9a86,#6e5a4a)"></div>
  <p class="card-title">Lorem ipsum dolor</p>
  <p class="card-text">Lorem ipsum dolor sit amet, con sectetuer adipiscing elit, sed diam nonummy nibh.</p>
  <span class="pay-btn">Pay Rent &#187;</span>
</article>
<article class="abs card" style="left:218px">
  <div class="card-photo" role="img" aria-label="Church spire above town green" style="background:linear-gradient(170deg,#8fb0d0,#7a8a6a)"></div>
  <p class="card-title">Lorem ipsum dolor</p>
  <p class="card-text">Lorem ipsum dolor sit amet, con sectetuer adipiscing elit, sed diam nonummy nibh.</p>
  <span class="pay-btn">Pay Rent &#187;</span>
</article>
<article class="abs card" style="left:360px">
  <div class="card-photo" role="img" aria-label="Park lawn and trees in summer" style="background:linear-gradient(170deg,#a9c6d8,#5f8a4a)"></div>
  <p class="card-title">Lorem ipsum dolor</p>
  <p class="card-text">Lorem ipsum dolor sit amet, con sectetuer adipiscing elit, sed diam nonummy nibh.</p>
  <span class="pay-btn">Pay Rent &#187;</span>
</article>
<article class="abs card" style="left:500px">
  <div class="card-photo" role="img" aria-label="Brick campus buildings" style="background:linear-gradient(170deg,#9fb5c6,#8b5e48)"></div>
  <p class="card-title">Lorem ipsum dolor</p>
  <p class="card-text">Lorem ipsum dolor sit amet, con sectetuer adipiscing elit, sed diam nonummy nibh.</p>
  <span class="pay-btn">Pay Rent &#187;</span>
</article>

<section class="abs lower" role="img" aria-label="Faint street map of the city"></section>

<form class="abs panel" style="left:78px;width:254px">
  <h3 class="panel-head">QUICK INQUIRY</h3>
  <p class="panel-sub">Lorem ipsum dolor sit amet, consectetuer adipiscing elit sed diam.</p>
  <div class="field">Full Name</div>
  <div class="field">Email</div>
  <div class="field">Phone</div>
  <div class="field tall">Message</div>
  <span class="submit">SUBMIT</span>
</form>

<div class="abs panel" style="left:367px;width:261px;height:150px">
  <h3 class="panel-head">CONTACT INFO</h3>
  <div class="contact-row">
    <svg viewBox="0 0 24 24"><circle cx="12" cy="12" r="12" fill="#3a3f45"/><path d="M12 5a4.5 4.5 0 0 0-4.5 4.5C7.5 13 12 19 12 19s4.5-6 4.5-9.5A4.5 4.5 0 0 0 12 5zm0 6.2a1.7 1.7 0 1 1 0-3.4 1.7 1.7 0 0 1 0 3.4z" fill="#fff"/></svg>
    <p>Street Name, City Name Dolor Sit Amet<br>Consectetuer Adipiscing 01234</p>
  </div>
  <div class="contact-row">
    <svg viewBox="0 0 24 24"><circle cx="12" cy="12" r="12" fill="#3a3f45"/><path d="M8.5 6.5l2 2.7-1.2 1.4c.7 1.5 1.9 2.7 3.4 3.4l1.4-1.2 2.7 2-1 2.2c-4.3-.3-7.9-3.9-8.2-8.2z" fill="#fff"/></svg>
    <p>012-345-6789</p>
  </div>
  <div class="contact-row">
    <svg viewBox="0 0 24 24"><circle cx="12" cy="12" r="12" fill="#3a3f45"/><rect x="6.5" y="8" width="11" height="8" fill="none" stroke="#fff" stroke-width="1.4"/><path d="M6.5 8l5.5 4.5L17.5 8" fill="none" stroke="#fff" stroke-width="1.4"/></svg>
    <p>info@qwrb-holdings.com</p>
  </div>
</div>

<footer class="abs footer"></footer>
<nav class="abs footer-links"><span>Home</span><span>About</span><span>Holdings</span><span>Contact Us</span></nav>
<p class="abs copyright">&copy; 2016 QWRB HOLDINGS - All Rights Reserved</p>
<p class="abs footer-brand">QWRB HOLDINGS</p>
<div class="abs social-foot"><span></span><span></span><span></span></div>

</body>
</html>
```